Webpage for balustrade importer and installer

We are a balustrade importer and installer. We sell a few different products mostly connected with glass and aluminum. We sell balconies, stairs, shower glass, mirrors, splash back glass, office partitions, glass dors and walls.

Coded - Design and coding required

```html
<!DOCTYPE html>
<html lang="en">
<head>
<meta charset="utf-8">
<title>Fjordgler – Glass &amp; Aluminium Balustrades</title>
<link href="https://fonts.googleapis.com/css2?family=Oswald:wght@300;400&family=Quicksand:wght@400;500&display=swap" rel="stylesheet">
<style>
:root{
  --blue:#253f94;
  --blue-dark:#1d3380;
  --ink:#2b2b2b;
  --grey:#6b6b6b;
  --line:#e3e3e3;
  --star:#d9921a;
  --footer:#222222;
  --white:#ffffff;
}
*{box-sizing:border-box;margin:0;padding:0}
html,body{width:1200px;height:3684px;overflow:hidden}
body{font-family:"Quicksand",sans-serif;color:var(--ink);background:var(--white);position:relative}
a{color:inherit;text-decoration:none}

/* header */
.site-header{height:113px;display:flex;align-items:center;padding:0 110px;position:relative}
.brand{font-family:"Oswald",sans-serif;font-weight:300;font-size:52px;color:var(--blue);letter-spacing:-1px;line-height:1}
.main-nav{position:absolute;right:178px;top:0;height:113px;display:flex;align-items:center;gap:44px}
.main-nav a{font-family:"Oswald",sans-serif;font-weight:300;font-size:15px;color:var(--ink);text-transform:uppercase;white-space:nowrap}
.main-nav a.active{color:var(--blue)}
.cart-btn{position:absolute;left:1033px;top:33px;width:54px;height:54px;border-radius:50%;background:var(--blue);display:flex;align-items:center;justify-content:center}

/* hero */
.hero{height:701px;position:relative;text-align:center;color:var(--white);
  background:linear-gradient(180deg,#1c2a45 0%,#2d4262 35%,#3b5573 55%,#5d7896 80%,#8ea6bd 100%)}
.hero h1{position:absolute;top:225px;left:0;right:0;font-family:"Oswald",sans-serif;font-weight:300;font-size:112px;line-height:1;letter-spacing:-2px}
.hero p{position:absolute;top:378px;left:0;right:0;font-family:"Oswald",sans-serif;font-weight:300;font-size:20px;line-height:33px;text-transform:uppercase}
.btn-solid{position:absolute;left:518px;top:463px;width:164px;height:50px;background:var(--blue);color:var(--white);font-family:"Oswald",sans-serif;font-weight:300;font-size:21px;display:flex;align-items:center;justify-content:center;text-transform:uppercase}

/* categories */
.categories{height:156px;display:flex;border-bottom:1px solid var(--line);box-shadow:0 3px 6px rgba(0,0,0,.06)}
.category{width:150px;display:flex;flex-direction:column;align-items:center;padding-top:22px;position:relative;font-size:17px;color:#3a3a3a;text-align:center;line-height:20px}
.category+.category::before{content:"";position:absolute;left:0;top:16px;height:108px;border-left:2px solid var(--line)}
.category svg{width:56px;height:56px;margin-bottom:8px;fill:none;stroke:#3a3a3a;stroke-width:1.6}

/* section titles */
.section-title{text-align:center;font-family:"Oswald",sans-serif;font-weight:300;font-size:58px;line-height:1;color:var(--ink)}
.section-title span{color:var(--blue)}
.title-rule{width:70px;height:2px;background:var(--blue);margin:0 auto}

/* products */
.products{position:relative;height:655px}
.products .section-title{position:absolute;top:52px;left:0;right:0}
.products .title-rule{position:absolute;top:132px;left:565px}
.product-grid{position:absolute;top:176px;left:112px;display:flex;gap:17px}
.product-card{width:231px;height:403px;border:1px solid var(--line);box-shadow:0 1px 4px rgba(0,0,0,.08);padding:8px;text-align:center}
.product-media{height:185px}
.price{font-family:"Oswald",sans-serif;font-weight:400;font-size:25px;color:var(--blue);margin-top:23px;line-height:1}
.product-name{font-family:"Oswald",sans-serif;font-weight:300;font-size:23px;margin-top:12px;text-transform:uppercase;line-height:1}
.stars{margin-top:14px;color:var(--star);font-size:14px;letter-spacing:2px}
.btn-outline{display:inline-flex;align-items:center;justify-content:center;width:150px;height:42px;border:1px solid var(--blue);margin-top:15px;font-family:"Oswald",sans-serif;font-weight:300;font-size:15px;text-transform:uppercase;color:var(--ink)}

/* about */
.about{height:560px;position:relative;background:var(--blue);color:var(--white)}
.about-media{position:absolute;left:0;top:0;width:780px;height:560px;
  background:linear-gradient(90deg,#2c3442 0%,#4a5566 40%,rgba(80,95,125,.8) 70%,rgba(37,63,148,0) 100%),linear-gradient(180deg,#8d9bb4 0%,#3d4657 60%,#2a2e36 100%)}
.about h2{position:absolute;left:691px;top:100px;font-family:"Oswald",sans-serif;font-weight:300;font-size:58px;line-height:1;text-transform:uppercase}
.about .rule{position:absolute;left:692px;top:171px;width:70px;height:3px;background:var(--white)}
.about p{position:absolute;left:691px;top:206px;width:384px;font-size:13.5px;line-height:25.7px;text-align:justify}
.about .btn-outline{position:absolute;left:692px;top:397px;width:155px;height:52px;margin:0;border-color:var(--white);color:var(--white);font-size:21px}

/* gallery */
.gallery{height:668px;position:relative}
.gallery .section-title{position:absolute;top:50px;left:0;right:0}
.gallery .title-rule{position:absolute;top:128px;left:565px}
.gallery-grid{position:absolute;top:175px;left:112px;width:975px;height:431px;display:grid;grid-template-columns:repeat(4,1fr);grid-template-rows:1fr 1fr;gap:11px}
.g1{grid-column:1/3;grid-row:1;background:linear-gradient(180deg,#b7c0cc,#5a616b 60%,#3b3f47)}
.g2{grid-column:3;grid-row:1/3;background:linear-gradient(180deg,#bfc7c4,#777b78 45%,#4a3b30 100%)}
.g3{grid-column:4;grid-row:1;background:linear-gradient(160deg,#3b4354,#6f737c 60%,#b7b3ab)}
.g4{grid-column:1;grid-row:2;background:linear-gradient(180deg,#8b8f96,#5d5f63 60%,#9a8b74)}
.g5{grid-column:2;grid-row:2;background:linear-gradient(180deg,#7d8aa3,#d6a87e 40%,#4b4f59 60%,#2f333b)}
.g6{grid-column:4;grid-row:2;background:linear-gradient(180deg,#c9ced6,#6a7282 50%,#3b4253)}

/* testimonial */
.testimonial{height:484px;position:relative;background:var(--blue);color:var(--white)}
.portrait{position:absolute;left:146px;top:76px;width:352px;height:352px;border-radius:50%;background:radial-gradient(circle at 50% 40%,#f2f2f0,#d9d7d3 70%,#bdbab5)}
.quote-box{position:absolute;left:538px;top:100px;width:515px;height:288px;border:3px solid var(--white)}
.quote-mark{position:absolute;left:55px;top:-34px;padding:0 14px;background:var(--blue);font-family:"Oswald",sans-serif;font-weight:400;font-size:60px;line-height:60px}
.quote-box p{position:absolute;left:28px;top:38px;width:450px;font-size:14px;line-height:32px}
.quote-author{position:absolute;left:28px;top:208px;font-size:17px;display:flex;gap:14px;align-items:center}
.quote-author .stars{margin:0;color:var(--star)}
.quote-box .btn-outline{position:absolute;left:371px;top:257px;width:106px;height:45px;margin:0;background:var(--blue);border:3px solid var(--white);color:var(--white);font-family:"Quicksand",sans-serif;font-size:13px}

/* footer */
.site-footer{height:347px;background:var(--footer);color:var(--white);position:relative;text-align:center}
.site-footer .brand{color:var(--white);font-size:74px;position:absolute;top:40px;left:0;right:0}
.footer-nav{position:absolute;top:152px;left:0;right:0;display:flex;justify-content:center;gap:46px}
.footer-nav a{color:var(--white);font-family:"Oswald",sans-serif;font-weight:300;font-size:16px;text-transform:uppercase}
.social{position:absolute;top:213px;left:0;right:0;display:flex;justify-content:center;gap:7px}
.social span{width:37px;height:37px;border:2px solid var(--white);border-radius:50%;display:block}
.copyright{position:absolute;top:282px;left:0;right:0;font-size:13px}
</style>
</head>
<body>

<header class="site-header">
  <div class="brand">FJORDGLER</div>
  <nav class="main-nav">
    <a class="active" href="#">Home</a>
    <a href="#">About Us</a>
    <a href="#">Services</a>
    <a href="#">Product</a>
    <a href="#">Gallery</a>
    <a href="#">Contact Us</a>
  </nav>
  <a class="cart-btn" href="#" aria-label="Cart">
    <svg width="18" height="16" viewBox="0 0 18 16"><path d="M1 1h3l2 9h9l2-6H5" fill="none" stroke="#fff" stroke-width="2"/><circle cx="7" cy="13.5" r="1.5" fill="#fff"/><circle cx="14" cy="13.5" r="1.5" fill="#fff"/></svg>
  </a>
</header>

<section class="hero" role="img" aria-label="Snowy rooftop terrace with glass balustrade overlooking a city at dusk">
  <h1>FJORDGLER</h1>
  <p>Sed ut perspiciatis unde omnis iste natus error sit voluptatem<br>accusantium doloremque laudantium</p>
  <a class="btn-solid" href="#">Read More</a>
</section>

<nav class="categories">
  <div class="category"><svg viewBox="0 0 56 56"><circle cx="28" cy="9" r="5"/><circle cx="28" cy="19" r="4"/><path d="M22 26h12M28 26c-6 8-6 14 0 20c6-6 6-12 0-20M22 48h12"/></svg>Balconies</div>
  <div class="category"><svg viewBox="0 0 56 56"><path d="M4 50h48V8H44v10H34v10H24v10H14v12M4 50V40l40-32"/></svg>Stairs</div>
  <div class="category"><svg viewBox="0 0 56 56"><rect x="10" y="6" width="36" height="44"/><path d="M10 14h36M28 14v36M22 30v6M34 30v6"/></svg>Shower Glass</div>
  <div class="category"><svg viewBox="0 0 56 56"><circle cx="28" cy="22" r="16"/><circle cx="28" cy="22" r="12"/><path d="M20 28l14-14M24 32l12-12M28 38v8M18 48h20"/></svg>Mirrors</div>
  <div class="category"><svg viewBox="0 0 56 56"><circle cx="28" cy="28" r="8"/><path d="M28 8v8M28 40v8M8 28h8M40 28h8M14 14l6 6M36 36l6 6M42 14l-6 6M20 36l-6 6"/></svg>Splash Back<br>Glass</div>
  <div class="category"><svg viewBox="0 0 56 56"><rect x="12" y="6" width="20" height="44"/><rect x="32" y="22" width="14" height="28"/><path d="M17 14h4M24 14h4M17 22h4M24 22h4M17 30h4M24 30h4M36 30h6M36 38h6M20 50v-8h4v8"/></svg>Office<br>Partitions</div>
  <div class="category"><svg viewBox="0 0 56 56"><path d="M14 50V6h28v44M8 50h40M20 10l14-4v44l-14-2z"/><circle cx="30" cy="28" r="1.5"/></svg>Glass Doors</div>
  <div class="category"><svg viewBox="0 0 56 56"><path d="M6 14h44v28H6zM6 21h44M6 28h44M6 35h44M18 14v7M32 14v7M12 21v7M26 21v7M40 21v7M18 28v7M32 28v7M12 35v7M26 35v7M40 35v7"/></svg>Walls</div>
</nav>

<section class="products">
  <h2 class="section-title">OUR <span>PRODUCTS</span></h2>
  <div class="title-rule"></div>
  <div class="product-grid">
    <article class="product-card">
      <div class="product-media" role="img" aria-label="Glass balustrade panel with steel handrail" style="background:linear-gradient(180deg,#e8e6e3,#cfcbc6 70%,#2a2a2a 85%,#b58d62)"></div>
      <div class="price">$25.99</div><div class="product-name">Product Name</div>
      <div class="stars">☆☆☆☆☆</div><a class="btn-outline" href="#">View Deatils</a>
    </article>
    <article class="product-card">
      <div class="product-media" role="img" aria-label="Glass terrace railing above a lake" style="background:linear-gradient(180deg,#9fb0a8,#6d8597 40%,#4f6b82 100%)"></div>
      <div class="price">$25.99</div><div class="product-name">Product Name</div>
      <div class="stars">☆☆☆☆☆</div><a class="btn-outline" href="#">View Deatils</a>
    </article>
    <article class="product-card">
      <div class="product-media" role="img" aria-label="Floating wooden staircase with glass railing" style="background:linear-gradient(135deg,#f3f1ec,#e3ddd2 50%,#c8814a 75%,#e7e2da)"></div>
      <div class="price">$25.99</div><div class="product-name">Product Name</div>
      <div class="stars">☆☆☆☆☆</div><a class="btn-outline" href="#">View Deatils</a>
    </article>
    <article class="product-card">
      <div class="product-media" role="img" aria-label="Rooftop deck with frameless glass balustrade" style="background:linear-gradient(180deg,#7a6a52,#8b8172 35%,#8d9096 60%,#5f6670)"></div>
      <div class="price">$25.99</div><div class="product-name">Product Name</div>
      <div class="stars">☆☆☆☆☆</div><a class="btn-outline" href="#">View Deatils</a>
    </article>
  </div>
</section>

<section class="about">
  <div class="about-media" role="img" aria-label="House with aluminium balcony railing"></div>
  <h2>About Fjordgler</h2>
  <div class="rule"></div>
  <p>Sed ut perspiciatis unde omnis iste natus error sit voluptatem accusantium doloremque laudantium, totam rem aperiam, eaque ipsa quae ab illo inventore veritatis et quasi architecto beatae vitae dicta sunt explicabo. Nemo enim ipsam voluptatem quia voluptas sit aspernatur aut odit aut fugit, sed dolores eos qui ratione voluptatem sequi nesciunt.</p>
  <a class="btn-outline" href="#">Read More</a>
</section>

<section class="gallery">
  <h2 class="section-title">PHOTO <span>GALLERY</span></h2>
  <div class="title-rule"></div>
  <div class="gallery-grid">
    <div class="g1" role="img" aria-label="Terrace with dark aluminium railing in winter"></div>
    <div class="g2" role="img" aria-label="Interior staircase with glass balustrade"></div>
    <div class="g3" role="img" aria-label="Outdoor steel staircase beside a house"></div>
    <div class="g4" role="img" aria-label="Open-plan interior with glass stair railing"></div>
    <div class="g5" role="img" aria-label="Glass balcony at sunset over the sea"></div>
    <div class="g6" role="img" aria-label="House exterior with balcony railing"></div>
  </div>
</section>

<section class="testimonial">
  <div class="portrait" role="img" aria-label="Portrait of a smiling customer"></div>
  <div class="quote-box">
    <div class="quote-mark">“</div>
    <p>Sed ut perspiciatis unde omnis iste natus error sit vol uptatem acc usantium doloremque laudantium, totam rem aperiam, eaque ipsa quae ab illo inventore veritat is et quasi architecto beatae vitae dicta sunt explicabo. Nemo enim ipsam volupt atem quia voluptas sit aspernatur aut odit aut fugit...</p>
    <div class="quote-author">-ANNA BERG <span class="stars">☆☆☆☆☆</span></div>
    <a class="btn-outline" href="#">READ MORE</a>
  </div>
</section>

<footer class="site-footer">
  <div class="brand">FJORDGLER</div>
  <nav class="footer-nav">
    <a href="#">Home</a><a href="#">About Us</a><a href="#">Services</a><a href="#">Product</a><a href="#">Gallery</a><a href="#">Contact Us</a>
  </nav>
  <div class="social"><span></span><span></span><span></span><span></span><span></span></div>
  <div class="copyright">© Copyrights 2020-Fjordgler.All Rights Reserved.</div>
</footer>

</body>
</html>
```